One slide graphic for website

I am designing a series of sliders for my website http://new.kelmarbyte.com

The slide I am trying to create has the following message:

EVERY company is a media company.
Empower yours now!

Learn More >

The ideas I have had for imagery are an office building with the letters 'Every Company is a Media Company' either shone onto the building or letters on the building roof ledge ect.

Aby ideas you may have to improve on this would be appreciated.

The idea behind the slide is to promote a software application which gives marketing professionals the chance to increase their media coverage. The message also encourages companies to create their own news on a number of platforms as the media landscape has changed so much. Look at the blue finch stunt whereby they generated 10 million views on viddlo using PR alone.

Good luck and I look forward to seeing your ideas.

Marcus

```html
<!DOCTYPE html>
<html lang="en">
<head>
<meta charset="utf-8">
<title>Kelmarbyte – Every company is a media company</title>
<link href="https://fonts.googleapis.com/css2?family=Open+Sans:ital,wght@0,300;0,400;0,600;0,700;1,300;1,400;1,700&family=Oswald:wght@300;400&display=swap" rel="stylesheet">
<style>
  :root{
    --green:#23933f;
    --green-dark:#1c7a33;
    --green-nav:#24923f;
    --orange:#f7941d;
    --orange-light:#fbad35;
    --purple:#8e44ad;
    --teal:#20a3a0;
    --ink:#444;
    --ink-soft:#555;
    --grey-icon:#555;
    --white:#fff;
    --rule:#e6e6e6;
  }
  *{box-sizing:border-box;margin:0;padding:0}
  html,body{width:1200px;height:874px;overflow:hidden;background:var(--white)}
  body{font-family:"Open Sans",Arial,sans-serif;color:var(--ink);position:relative}

  .site-header{position:absolute;left:0;top:0;width:1200px;height:110px}
  .brand{position:absolute;left:153px;top:32px;display:flex;align-items:center;gap:8px;
    font-weight:600;font-size:36px;letter-spacing:-0.5px;color:var(--green)}
  .brand-dot{width:14px;height:14px;border-radius:50%;background:var(--green)}
  .contact{position:absolute;right:164px;top:18px;display:flex;align-items:center;gap:6px}
  .phone{font-size:19px;color:#666;margin-right:6px}
  .social{width:20px;height:20px;border-radius:50%;background:var(--grey-icon)}
  .header-actions{position:absolute;right:164px;top:51px;display:flex;gap:6px}
  .pill{display:flex;align-items:center;gap:6px;height:26px;padding:0 10px 0 6px;border-radius:9px;
    color:var(--white);font-weight:700;font-style:italic;font-size:15px;text-transform:uppercase}
  .pill-demo{background:var(--purple);width:126px}
  .pill-login{background:var(--orange);width:88px}
  .pill svg{flex:none}

  .main-nav{position:absolute;left:0;top:109px;width:1200px;height:47px;background:var(--green-nav);
    border-top:4px solid var(--green-dark)}
  .main-nav ul{list-style:none;display:flex;position:absolute;left:153px;top:0;height:43px}
  .main-nav li{display:flex;align-items:center;padding:0 11px;height:43px;color:var(--white);
    font-weight:700;font-size:12.5px;text-transform:uppercase;border-right:1px solid rgba(0,0,0,.18)}
  .main-nav li.is-active{background:var(--orange)}

  .hero{position:absolute;left:0;top:156px;width:1200px;height:411px;overflow:hidden;
    background:
      linear-gradient(180deg,rgba(255,255,255,0) 55%,rgba(230,232,236,.9) 82%,#e8eaee 100%),
      linear-gradient(100deg,#e07a2a 0%,#f0913c 30%,#f3a867 55%,#d9b7a4 75%,#c9c6cc 100%)}
  .hero-art{position:absolute;left:20px;top:40px;width:590px;height:350px;
    background:
      radial-gradient(ellipse 48% 46% at 50% 56%,rgba(55,60,70,.55) 0%,rgba(80,85,95,.35) 55%,rgba(120,125,135,0) 100%)}
  .hero-title{position:absolute;left:570px;top:70px;width:640px;text-align:center;
    font-family:"Oswald",sans-serif;font-weight:300;font-size:45px;line-height:58px;color:var(--white);
    text-shadow:2px 2px 3px rgba(0,0,0,.55)}
  .hero-cta{position:absolute;left:958px;top:359px;width:165px;height:36px;border-radius:8px;
    background:linear-gradient(180deg,var(--orange-light),var(--orange));display:flex;align-items:center;gap:8px;padding-left:6px;
    font-family:"Oswald",sans-serif;font-weight:300;font-size:27px;color:var(--white);
    box-shadow:1px 2px 3px rgba(0,0,0,.3)}
  .hero-band{position:absolute;left:0;top:567px;width:1200px;height:9px;background:var(--teal)}

  .tagline{position:absolute;left:0;top:588px;width:1200px;text-align:center;
    font-style:italic;font-weight:300;font-size:32px;line-height:36px;color:var(--ink)}

  .features{position:absolute;left:153px;top:696px;display:flex}
  .feature{width:225px;height:200px;text-align:center;border-left:1px solid var(--rule);border-right:1px solid var(--rule)}
  .feature h3{font-style:italic;font-weight:400;font-size:17px;color:var(--ink);margin-top:4px;height:38px}
  .feature svg{display:block;margin:0 auto;height:68px}
  .feature p{font-style:italic;font-size:12.5px;line-height:19px;color:var(--ink-soft);margin:10px 22px 0}
  .feature p.narrow{margin:10px 30px 0}
</style>
</head>
<body>
  <header class="site-header">
    <div class="brand"><span class="brand-dot"></span>KELMARBYTE</div>
    <div class="contact">
      <span class="phone">t. +44 (0)1632 960418</span>
      <span class="social"></span><span class="social"></span><span class="social"></span>
    </div>
    <div class="header-actions">
      <span class="pill pill-demo"><svg width="18" height="18" viewBox="0 0 18 18"><circle cx="9" cy="9" r="9" fill="#fff"/><path d="M5 9h7M9 5.5 12.5 9 9 12.5" stroke="#8e44ad" stroke-width="2" fill="none"/></svg>Free Demo</span>
      <span class="pill pill-login"><svg width="18" height="18" viewBox="0 0 18 18"><circle cx="9" cy="9" r="9" fill="#fff"/><path d="M5 9h7M9 5.5 12.5 9 9 12.5" stroke="#f7941d" stroke-width="2" fill="none"/></svg>Login</span>
    </div>
  </header>

  <nav class="main-nav">
    <ul>
      <li class="is-active">Home</li><li>Our Offer</li><li>Who We Work With</li><li>News</li>
      <li>Webinars</li><li>Free Downloads</li><li>Who We Are</li><li>Our Values</li><li>About Us</li>
    </ul>
  </nav>

  <section class="hero">
    <div class="hero-art" role="img" aria-label="3D render of a modern glass pavilion with a large social media billboard on its roof"></div>
    <h1 class="hero-title">EVERY company is a media company.<br>Empower yours now!</h1>
    <a class="hero-cta"><svg width="24" height="24" viewBox="0 0 24 24"><circle cx="12" cy="12" r="11" fill="none" stroke="#fff" stroke-width="2"/><path d="M6.5 12h10M12 7.5l4.5 4.5-4.5 4.5" stroke="#fff" stroke-width="2.2" fill="none"/></svg>Learn More</a>
  </section>
  <div class="hero-band"></div>

  <p class="tagline">Kelmarbyte is the most efficient way to distribute your news and<br>nurture your reputation.</p>

  <section class="features">
    <svg width="0" height="0" style="position:absolute"><defs>
      <linearGradient id="icon-grad" x1="0" y1="0" x2="0" y2="1"><stop offset="0" stop-color="#26b08a"/><stop offset="1" stop-color="#1f9a3e"/></linearGradient>
    </defs></svg>
    <div class="feature">
      <h3>Targeted Distribution</h3>
      <svg width="64" height="68" viewBox="0 0 64 68"><g fill="url(#icon-grad)">
        <ellipse cx="32" cy="10" rx="30" ry="10"/><path d="M2 16c0 6 13 10 30 10s30-4 30-10v12c0 6-13 10-30 10S2 34 2 28z"/>
        <path d="M2 34c0 6 13 10 30 10s30-4 30-10v12c0 6-13 10-30 10S2 52 2 46z"/><path d="M2 52c0 6 13 10 30 10s30-4 30-10v6c0 6-13 10-30 10S2 64 2 58z"/></g></svg>
      <p>Source from a UK media database and distribute your messages to relevant media</p>
    </div>
    <div class="feature">
      <h3>Stakeholder Relations</h3>
      <svg width="72" height="68" viewBox="0 0 72 68"><path d="M0 4h26l6 7h40v57H0z" fill="url(#icon-grad)"/>
        <rect x="28" y="28" width="30" height="22" fill="none" stroke="#fff" stroke-width="2.5"/><path d="M28 28l15 12 15-12" fill="none" stroke="#fff" stroke-width="2.5"/>
        <path d="M12 33h12M15 39h9M18 45h6" stroke="#fff" stroke-width="2.5"/></svg>
      <p>News e-shot function extends your organisation’s reach to influence key stakeholders.</p>
    </div>
    <div class="feature">
      <h3>Virtual Newsroom</h3>
      <svg width="68" height="68" viewBox="0 0 72 72"><path d="M36 6a30 30 0 1 1-21 9" fill="none" stroke="url(#icon-grad)" stroke-width="7"/>
        <path d="M8 4l16 4-10 12z" fill="#1f9a3e"/><path d="M36 18v20h14" fill="none" stroke="#1f9a3e" stroke-width="6"/></svg>
      <p class="narrow">Enhanced newsroom technology allows you to push your content straight into the</p>
    </div>
    <div class="feature">
      <h3>Secure and Safe</h3>
      <svg width="92" height="68" viewBox="0 0 92 68"><path d="M20 62a18 18 0 0 1-2-36A26 26 0 0 1 68 20a20 20 0 0 1 4 42z" fill="url(#icon-grad)"/>
        <path d="M46 22l-16 16h10v20h12V38h10z" fill="#fff"/></svg>
      <p>Cloud-based PR tools hosted on secure and dedicated Cloudvault servers.</p>
    </div>
  </section>
</body>
</html>
```